Candle Labels for 9 oz tumbler soy candles

Looking for new label design for my candle business. Currently, using a label I designed that needs to be more professional rather than looking homemade. Wanting a professional, clean looking label that enhances my product line. My candle tumblers are white and at times I also use tin containers for my candles so wanting something that will provide a modern/elegant feel to them

Industry/Entity Type

Business

Font styles to use
Decorative
Script

Colors

Designer to choose colors to be used in the design.

Requirements
Must have
• My logo, net weight 9 oz, Space for the name of the Candle (one example is Velvet Dunes
• Looking for something sleek and clean looking, no clutter
Nice to have
• website url www.amberhollowwick.shopnest.com, words "Soy Candle" on the label

```html
<!DOCTYPE html>
<html lang="en">
<head>
<meta charset="utf-8">
<title>Velvet Dunes Soy Candle Label</title>
<link href="https://fonts.googleapis.com/css2?family=Original+Surfer&family=Righteous&family=Roboto:wght@400;500&display=swap" rel="stylesheet">
<style>
  :root {
    --bg: #ffffff;
    --ring-green: #3f5a52;
    --ring-orange: #f5a733;
    --ink-green: #3d564f;
    --ink-orange: #f5a733;
    --ribbon: #f5a733;
    --ribbon-ink: #3d564f;
  }
  * { margin: 0; padding: 0; box-sizing: border-box; }
  html, body {
    width: 1200px; height: 922px; overflow: hidden;
    background: var(--bg);
  }
  .canvas { position: relative; width: 1200px; height: 922px; }
  .label-rings { position: absolute; left: 0; top: 0; }
  .brand {
    position: absolute; left: 0; width: 1200px; top: 280px;
    display: flex; justify-content: center; align-items: center; gap: 12px;
    font-family: "Roboto", sans-serif; font-weight: 500; font-size: 40px;
    color: var(--ink-green); letter-spacing: 0.5px;
  }
  .brand-dot {
    width: 16px; height: 16px; border-radius: 50%; background: var(--ink-orange);
  }
  .candle-name {
    position: absolute; left: 0; width: 1200px; top: 375px;
    text-align: center;
    font-family: "Original Surfer", cursive; font-size: 80px; line-height: 1;
    color: var(--ink-green);
  }
  .ribbon { position: absolute; left: 343px; top: 523px; }
  .ribbon-text {
    position: absolute; left: 343px; top: 523px; width: 515px; height: 60px;
    display: flex; align-items: center; justify-content: center;
    font-family: "Righteous", sans-serif; font-size: 42px; letter-spacing: 1px;
    color: var(--ribbon-ink);
  }
  .site {
    position: absolute; left: 0; width: 1200px; top: 614px;
    text-align: center;
    font-family: "Roboto", sans-serif; font-weight: 500; font-size: 25px;
    color: var(--ink-green);
  }
  .net-weight {
    position: absolute; left: 0; width: 1200px; top: 678px;
    text-align: center;
    font-family: "Roboto", sans-serif; font-weight: 400; font-size: 33px;
    color: var(--ink-orange);
  }
</style>
</head>
<body>
  <main class="canvas">
    <svg class="label-rings" width="1200" height="922" viewBox="0 0 1200 922" aria-hidden="true">
      <circle cx="600" cy="461" r="350" fill="none" stroke="var(--ring-green)" stroke-width="4"/>
      <circle cx="600" cy="461" r="337" fill="none" stroke="var(--ring-orange)" stroke-width="3.5"/>
    </svg>

    <div class="brand"><span class="brand-dot"></span>Amber Hollow Wick</div>

    <h1 class="candle-name">Velvet Dunes</h1>

    <svg class="ribbon" width="515" height="60" viewBox="0 0 515 60" aria-hidden="true">
      <polygon points="0,0 515,0 490,30 515,60 0,60 25,30" fill="var(--ribbon)"/>
    </svg>
    <div class="ribbon-text">SOY CANDLE</div>

    <p class="site">www.amberhollowwick.shopnest.com</p>
    <p class="net-weight">Net weight 9 oz</p>
  </main>
</body>
</html>
```